A4 Client Referral Program Flyer for Property Management Agency

Harbourline Lettings Group is a property management specialist based on Sydney's Northern Beaches in Australia.

We manage mid to high-end rental properties for investors and property owners.
We are currently looking to build our portfolio and are offering existing clients and contacts a referral incentive. We want to sign up more properties to manage.

We are offering the referrer a $250 referral fee and the new owner 2 months of free management to entice them to use Harbourline Lettings Group.

We want an A4 Flyer to print and add to other document packages we hand out to clients and suppliers.
If at all possible a matching digital banner would be great too! 1000px wide x 250px

Please find copy attached in Word Doc and our logo attached also.

Please see our website for any more details on our business.

We must be able to have an editable photoshop version (PSD) of the document as well as a print ready PDF version incl any bleed necessary for A4 printing.

Target Market(s)

30-60YO Male and Female

Industry/Entity Type

Real Estate

Font styles to use
Sans Serif

Requirements
Must have
• Company Logo, contact details and copy provided

```html
<!DOCTYPE html>
<html lang="en">
<head>
<meta charset="utf-8">
<title>Harbourline Lettings Group – Referral Flyer</title>
<link rel="stylesheet" href="https://fonts.googleapis.com/css2?family=Oswald:wght@300;400;700&family=Lato:wght@400;700&display=swap">
<style>
  :root {
    --page-bg: #e6e5e3;
    --paper: #ffffff;
    --mist: #eef0f2;
    --teal: #1596a8;
    --teal-light: #25b3c5;
    --teal-deep: #0e6774;
    --charcoal: #2a2a2c;
    --ink: #1d1d1f;
    --white: #ffffff;
  }
  * { box-sizing: border-box; margin: 0; padding: 0; }
  html, body { width: 1200px; height: 865px; overflow: hidden; }
  body {
    background: var(--page-bg);
    font-family: "Lato", Arial, sans-serif;
    color: var(--ink);
    position: relative;
  }
  .flyer {
    position: absolute;
    left: 308px; top: 20px;
    width: 583px; height: 825px;
    background: var(--paper);
    overflow: hidden;
    box-shadow: 0 6px 18px rgba(0,0,0,.18);
  }
  .intro-column {
    position: absolute; left: 0; top: 0;
    width: 300px; height: 270px;
    background: linear-gradient(180deg, var(--mist), #fbfbfc);
  }
  .brand {
    position: absolute; left: 26px; top: 44px;
    display: flex; align-items: center; gap: 10px;
  }
  .brand-dot {
    width: 14px; height: 14px; background: var(--teal);
  }
  .brand-name {
    font-family: "Oswald", Arial, sans-serif;
    font-weight: 400; font-size: 21px; letter-spacing: .5px;
    color: var(--ink); text-transform: uppercase; line-height: 1.1;
    width: 230px;
  }
  .headline {
    position: absolute; left: 22px; top: 128px; width: 266px;
    font-family: "Oswald", Arial, sans-serif;
    font-weight: 300; font-size: 25px; line-height: 1.18;
    text-align: center; color: var(--ink);
  }
  .hero-photo {
    position: absolute; right: 0; top: 0;
    width: 300px; height: 515px;
    clip-path: polygon(18px 0, 100% 0, 100% 100%, 0 100%);
    background: linear-gradient(180deg, #2f7fd6 0%, #7fb4e6 24%, #f4f5f4 40%, #d9d8d4 58%, #6e5a48 78%, #4a3a2c 100%);
  }
  .offer-panel {
    position: absolute; left: 0; top: 270px;
    width: 300px; height: 245px;
    background: linear-gradient(160deg, var(--teal-light), var(--teal) 55%, #0f8496);
  }
  .offer-lead {
    position: absolute; left: 0; top: 20px; width: 100%;
    text-align: center; font-weight: 700; font-size: 18px;
    color: var(--ink);
  }
  .burst {
    position: absolute; left: 70px; top: 52px;
    width: 158px; height: 158px;
  }
  .burst-text {
    position: absolute; inset: 0;
    display: flex; flex-direction: column; align-items: center; justify-content: center;
    font-family: "Oswald", Arial, sans-serif; font-weight: 700; color: var(--ink);
    line-height: .95;
  }
  .burst-text .receive { font-size: 28px; }
  .burst-text .amount { font-size: 50px; }
  .offer-strip {
    position: absolute; left: 0; top: 492px;
    width: 318px; height: 40px;
    background: var(--charcoal);
    clip-path: polygon(0 0, 100% 0, 96% 100%, 0 100%);
    color: var(--white); font-weight: 700; font-size: 15px;
    display: flex; align-items: center; padding-left: 16px;
  }
  .divider {
    position: absolute; left: 0; top: 542px;
    width: 300px; height: 8px; background: var(--teal);
  }
  .terms {
    position: absolute; left: 28px; top: 568px; width: 218px;
    font-size: 13px; line-height: 1.25; text-align: justify; color: var(--ink);
  }
  .gallery-band {
    position: absolute; left: 256px; top: 575px;
    width: 327px; height: 104px; background: var(--teal);
  }
  .gallery-photo {
    position: absolute; top: 560px;
    width: 142px; height: 128px;
    border: 6px solid var(--charcoal);
  }
  .gallery-photo.kitchen {
    left: 270px;
    background: linear-gradient(180deg, #9a6a45 0%, #c9976b 40%, #f1efec 62%, #d8d4cf 100%);
  }
  .gallery-photo.lounge {
    left: 424px;
    background: linear-gradient(180deg, #f6f5f3 0%, #e4e2de 50%, #8d8f92 78%, #b4a596 100%);
  }
  .contact-block {
    position: absolute; left: 0; top: 705px;
    width: 350px; height: 120px;
    background: var(--charcoal);
    clip-path: polygon(0 0, 82% 0, 100% 100%, 0 100%);
    color: var(--white);
    padding: 16px 0 0 22px;
  }
  .contact-line {
    display: flex; align-items: center; gap: 10px;
    font-size: 13px; margin-bottom: 6px;
  }
  .contact-line.web { font-size: 17px; font-weight: 700; }
  .contact-line svg { width: 17px; height: 17px; flex: none; }
  .accent-line {
    position: absolute; left: 330px; top: 760px;
    width: 253px; height: 8px; background: var(--teal-light);
  }
  .phone-bar {
    position: absolute; left: 340px; top: 768px;
    width: 243px; height: 57px; background: var(--teal-deep);
    color: var(--white);
    display: flex; align-items: center; gap: 10px; padding-left: 30px;
    font-size: 20px; font-weight: 700; letter-spacing: .5px;
  }
  .phone-bar svg { width: 24px; height: 24px; }
</style>
</head>
<body>
  <main class="flyer">
    <section class="intro-column">
      <div class="brand">
        <span class="brand-dot"></span>
        <span class="brand-name">Harbourline Lettings Group</span>
      </div>
      <h1 class="headline">Harbourline Lettings Group is specializing in property management</h1>
    </section>

    <div class="hero-photo" role="img" aria-label="Modern white two-storey home with timber deck, glass pool fence and palm under blue sky"></div>

    <section class="offer-panel">
      <p class="offer-lead">Invite your friends and</p>
      <div class="burst">
        <svg viewBox="0 0 100 100" width="158" height="158" aria-hidden="true">
          <defs>
            <linearGradient id="burstFill" x1="0" y1="0" x2="0" y2="1">
              <stop offset="0" stop-color="#ffffff"/>
              <stop offset="1" stop-color="#a9abae"/>
            </linearGradient>
          </defs>
          <polygon fill="url(#burstFill)" points="100,50 92.5,56.7 97.6,65.5 88.3,69.5 90.5,79.4 80.4,80.4 79.4,90.5 69.5,88.3 65.5,97.6 56.7,92.5 50,100 43.3,92.5 34.5,97.6 30.5,88.3 20.6,90.5 19.6,80.4 9.5,79.4 11.7,69.5 2.4,65.5 7.5,56.7 0,50 7.5,43.3 2.4,34.5 11.7,30.5 9.5,20.6 19.6,19.6 20.6,9.5 30.5,11.7 34.5,2.4 43.3,7.5 50,0 56.7,7.5 65.5,2.4 69.5,11.7 79.4,9.5 80.4,19.6 90.5,20.6 88.3,30.5 97.6,34.5 92.5,43.3"/>
        </svg>
        <div class="burst-text">
          <span class="receive">Receive</span>
          <span class="amount">$250</span>
        </div>
      </div>
    </section>

    <div class="offer-strip">and they get 2 months free management!</div>
    <div class="divider"></div>

    <p class="terms">$250 referral fee paid when the owner you refer signs their property for Management with Harbourline Lettings Group.</p>

    <div class="gallery-band"></div>
    <div class="gallery-photo kitchen" role="img" aria-label="Bright kitchen with timber cabinetry, white island and bar stools"></div>
    <div class="gallery-photo lounge" role="img" aria-label="Light living room with grey sofa, pendant lamp and artwork"></div>

    <footer>
      <div class="contact-block">
        <p class="contact-line">
          <svg viewBox="0 0 24 24" fill="none" stroke="currentColor" stroke-width="1.6"><rect x="3" y="6" width="18" height="12"/><path d="M3 6l9 7 9-7"/></svg>
          referrals@harbourlinelettings.com.au
        </p>
        <p class="contact-line web">
          <svg viewBox="0 0 24 24" fill="none" stroke="currentColor" stroke-width="1.6"><circle cx="12" cy="12" r="9"/><ellipse cx="12" cy="12" rx="4" ry="9"/><path d="M3 12h18M5 7h14M5 17h14"/></svg>
          www.harbourlinelettings.com.au
        </p>
      </div>
      <div class="accent-line"></div>
      <div class="phone-bar">
        <svg viewBox="0 0 24 24" fill="none" stroke="currentColor" stroke-width="1.6"><circle cx="12" cy="12" r="10.5"/><path d="M9 6.5l1.8 3-1.3 1.3c.8 1.6 1.9 2.7 3.5 3.5l1.3-1.3 3 1.8-.9 2.2c-4.7 0-9.4-4.7-9.4-9.4z" fill="currentColor" stroke="none"/></svg>
        0400 555 218
      </div>
    </footer>
  </main>
</body>
</html>
```